Etiketten-Design für familiengeführten Weinbaubetrieb
Zielgruppe
Wir sind ein Familiengeführter Weinbaubetrieb und vermarkten unseren Wein in 0,75l Flaschen sowie auch Säfte und Schnäpse.
Zur zeit Verkaufen wir unseren Wein an Gastro und Private Kunden auch teils über Messen
Aufgabenstellung
Das derzeitige Etikett ist recht schlicht gestaltet und das Logo besteht rein aus dem geschriebenen Namen Winzerhof Kellbrunner. Es kann aber auch gerne nur mit dem Namen Kellbrunner ohne Winzerhof gearbeitet werden! Mit dem einbringen einer neuen Generation in den Betrieb wollen wir das aussehen unserer Produkte erneuern. Dazu kann sich gerne mit dem Namen als 'Logo' in jeglicher Art gespielt werden. Wir füllen unsere Weine in 0,75l Bordeaux Flaschen. Die Form des Etikett ist kein K.O. Kriterium jedoch wurde ursprünglich ein rund um Etikett angedacht. Sollten die Designes sich auch anders realisieren lassen sind wir gerne offen für Ideen.

```html
<!DOCTYPE html>
<html lang="de">
<head>
<meta charset="utf-8">
<title>Winzerhof Kellbrunner – Etiketten</title>
<link href="https://fonts.googleapis.com/css2?family=Montserrat:wght@300;400;500&display=swap" rel="stylesheet">
<style>
  :root {
    --backdrop: #eeebe5;
    --label-white: #ffffff;
    --label-black: #1d1d1d;
    --leaf-green: #8cc21f;
    --leaf-green-dark: #5f8f12;
    --gold: #c99a1e;
    --gold-light: #e6c35a;
    --ink-grey: #5a5a5a;
    --ink-light: #bdbdbd;
    --badge-dark: #2a2a2a;
  }
  * { margin: 0; padding: 0; box-sizing: border-box; }
  html, body { width: 1200px; height: 971px; overflow: hidden; }
  body {
    background: var(--backdrop);
    font-family: "Montserrat", sans-serif;
    position: relative;
  }
  .label-row {
    position: absolute;
    top: 220px;
    left: 0;
    width: 1200px;
    display: flex;
    justify-content: center;
    gap: 40px;
  }
  .label {
    position: relative;
    width: 300px;
    height: 520px;
    box-shadow: 0 6px 24px rgba(0,0,0,0.12);
    display: flex;
    flex-direction: column;
    align-items: center;
  }
  .label--white { background: var(--label-white); }
  .label--black { background: var(--label-black); }

  .label__topline {
    position: absolute;
    left: 0; right: 0;
    top: 0;
    height: 4px;
  }
  .label--black .label__topline { height: 3px; }
  .label--green .label__topline { background: linear-gradient(90deg, var(--leaf-green-dark), var(--leaf-green), var(--leaf-green-dark)); }
  .label--gold .label__topline { background: linear-gradient(90deg, var(--gold), var(--gold-light), var(--gold)); }

  .brand {
    margin-top: 80px;
    display: flex;
    align-items: center;
    gap: 8px;
    font-weight: 400;
    font-size: 22px;
    letter-spacing: 1px;
    white-space: nowrap;
  }
  .brand__dot {
    width: 14px; height: 14px;
    border-radius: 50%;
    flex: none;
  }
  .label--green .brand { color: var(--leaf-green); }
  .label--green .brand__dot { background: var(--leaf-green); }
  .label--gold .brand { color: var(--gold); }
  .label--gold .brand__dot { background: var(--gold); }

  .wine-name {
    margin-top: 34px;
    text-align: center;
    font-weight: 400;
    font-size: 13px;
    letter-spacing: 7px;
    line-height: 1.55;
    padding-left: 7px;
  }
  .label--white .wine-name { color: var(--ink-grey); }
  .label--black .wine-name { color: var(--ink-light); }
  .vintage {
    margin-top: 20px;
    font-size: 10px;
    letter-spacing: 6px;
    padding-left: 6px;
  }
  .label--white .vintage { color: var(--ink-grey); }
  .label--black .vintage { color: var(--ink-light); }

  .region-badge {
    position: absolute;
    bottom: 58px;
    left: 50%;
    transform: translateX(-50%);
    width: 34px;
    height: 30px;
    border-radius: 4px;
  }
  .label--white .region-badge { background: var(--badge-dark); }
  .label--black .region-badge { background: #f2f2f2; }

  .label__band {
    position: absolute;
    left: 0; right: 0;
    bottom: 24px;
    height: 18px;
    display: flex;
    align-items: center;
    justify-content: center;
    font-size: 11px;
    font-weight: 500;
    letter-spacing: 5px;
    padding-left: 5px;
    text-transform: uppercase;
    white-space: nowrap;
  }
  .label--green .label__band {
    background: linear-gradient(90deg, var(--leaf-green-dark), var(--leaf-green), var(--leaf-green-dark));
    color: #d6f08e;
  }
  .label--gold .label__band {
    background: linear-gradient(90deg, var(--gold), var(--gold-light), var(--gold));
    color: #5b430a;
  }
  .label--black.label--gold .label__band { color: #1d1d1d; }
</style>
</head>
<body>
  <main class="label-row">
    <section class="label label--white label--green" aria-label="Etikett Weißwein">
      <div class="label__topline"></div>
      <div class="brand"><span class="brand__dot"></span>Kellbrunner</div>
      <div class="region-badge" aria-label="Herkunftssiegel"></div>
      <div class="label__band">Winzerhof Kellbrunner</div>
    </section>

    <section class="label label--white label--gold" aria-label="Etikett Grüner Veltliner">
      <div class="label__topline"></div>
      <div class="brand"><span class="brand__dot"></span>Kellbrunner</div>
      <p class="wine-name">GRÜNER<br>VELTLINER<br>DAC</p>
      <p class="vintage">2024</p>
      <div class="region-badge" aria-label="Herkunftssiegel"></div>
      <div class="label__band">Winzerhof Kellbrunner</div>
    </section>

    <section class="label label--black label--gold" aria-label="Etikett Zweigelt">
      <div class="label__topline"></div>
      <div class="brand"><span class="brand__dot"></span>Kellbrunner</div>
      <p class="wine-name">ZWEIGELT<br>KLASSIK</p>
      <p class="vintage">2024</p>
      <div class="region-badge" aria-label="Herkunftssiegel"></div>
      <div class="label__band">Winzerhof Kellbrunner</div>
    </section>
  </main>
</body>
</html>
```